Trade Show Backdrop

I need a fun and unique design using our colors and verbiage. I have uploaded an example of what was already created and as you can see, it's lame.
I need it to say the same thing, but I want a bit more flare to the layout and graphics.
I have also uploaded what the competition uses.
I would like a clean look, no pictures. Obviously it has to be scale for a 10x10 booth, stand and

Target Market(s)

Private, Commercial and Public

Font styles to use
Sans Serif

Colors
fbed22
ffffff

Requirements
Must have
• Yellow, Gray, Black & WhiteAsphalt background- uploaded

```html
<!DOCTYPE html>
<html lang="en">
<head>
<meta charset="utf-8">
<title>The Road Maven – Trade Show Backdrop</title>
<link href="https://fonts.googleapis.com/css2?family=Oswald:wght@300;400;500;600;700&display=swap" rel="stylesheet">
<style>
  :root {
    --yellow: #fbd40a;
    --white: #ffffff;
    --black: #111111;
    --asphalt-dark: #141414;
    --asphalt-mid: #2a2a2a;
    --ink: #1a1a1a;
  }
  * { margin: 0; padding: 0; box-sizing: border-box; }
  html, body { width: 1200px; height: 1020px; overflow: hidden; background: var(--white); }
  .backdrop { position: relative; width: 1200px; height: 1020px; overflow: hidden; font-family: "Oswald", sans-serif; }

  .asphalt {
    position: absolute; left: 0; top: 0; width: 1200px; height: 880px;
    background: radial-gradient(ellipse at 50% 40%, var(--asphalt-mid) 0%, var(--asphalt-dark) 75%);
  }

  .eyebrow {
    position: absolute; top: 46px; left: 0; width: 100%; text-align: center;
    color: var(--yellow); font-weight: 300; font-size: 54px; letter-spacing: -0.5px; line-height: 1;
  }
  .headline {
    position: absolute; top: 106px; left: 0; width: 100%; text-align: center;
    color: var(--white); font-weight: 700; font-size: 81px; line-height: 1; letter-spacing: 1px;
  }

  .services-title {
    position: absolute; left: 88px; top: 306px;
    color: var(--yellow); font-weight: 700; font-size: 54px; line-height: 1;
  }
  .service-list { position: absolute; list-style: none; }
  .service-list li {
    position: relative; height: 46px; display: flex; align-items: center;
    color: var(--white); font-weight: 500; font-size: 25px; letter-spacing: 1.5px;
  }
  .service-list li svg { width: 26px; height: 26px; margin-right: 14px; flex: none; }
  .service-list--left { left: 84px; top: 370px; }
  .service-list--right { left: 810px; top: 329px; }

  .brand-name {
    position: absolute; left: 420px; top: 308px; width: 342px; text-align: center;
    color: var(--yellow); font-weight: 700; font-size: 66px; line-height: 68px; letter-spacing: 1px;
  }

  .feature-band {
    position: absolute; left: 0; top: 641px; width: 1200px; height: 144px; background: var(--yellow);
  }
  .feature-icon {
    position: absolute; width: 94px; height: 94px; border-radius: 50%;
    background: var(--black); border: 5px solid var(--white); top: 594px;
  }
  .feature-icon svg { position: absolute; left: 20px; top: 20px; width: 44px; height: 44px; }
  .feature-label {
    position: absolute; top: 700px; width: 240px; text-align: center;
    color: var(--ink); font-weight: 500; font-size: 28px; line-height: 29px; letter-spacing: 0.5px;
  }
  .feature-divider { position: absolute; top: 704px; width: 2px; height: 62px; background: var(--ink); }

  .lane-line {
    position: absolute; left: 0; top: 820px; width: 1200px; height: 8px;
    background: repeating-linear-gradient(90deg, transparent 0 37px, var(--white) 37px 73px);
  }

  .website {
    position: absolute; top: 912px; left: 363px; width: 400px; text-align: center;
    color: var(--black); font-weight: 400; font-size: 41px; line-height: 1;
  }
  .social { position: absolute; top: 920px; left: 1010px; display: flex; gap: 14px; }
  .social span { width: 27px; height: 27px; background: var(--black); border-radius: 4px; }
</style>
</head>
<body>
<main class="backdrop">
  <div class="asphalt" role="img" aria-label="Dark asphalt texture background"></div>

  <p class="eyebrow">PAVEMENT SOLUTIONS</p>
  <h1 class="headline">CUSTOME MADE FOR YOU</h1>

  <h2 class="services-title">SERVICES</h2>
  <ul class="service-list service-list--left">
    <li><svg viewBox="0 0 26 26"><circle cx="13" cy="13" r="10.5" fill="none" stroke="#fbd40a" stroke-width="3"/><path d="M8 13.5l3.5 3.5 6.5-7" fill="none" stroke="#fbd40a" stroke-width="3"/></svg>SEALCOATING</li>
    <li><svg viewBox="0 0 26 26"><circle cx="13" cy="13" r="10.5" fill="none" stroke="#fbd40a" stroke-width="3"/><path d="M8 13.5l3.5 3.5 6.5-7" fill="none" stroke="#fbd40a" stroke-width="3"/></svg>CONCREAT CURBS</li>
    <li><svg viewBox="0 0 26 26"><circle cx="13" cy="13" r="10.5" fill="none" stroke="#fbd40a" stroke-width="3"/><path d="M8 13.5l3.5 3.5 6.5-7" fill="none" stroke="#fbd40a" stroke-width="3"/></svg>ASPHALT PAVINGS</li>
  </ul>

  <p class="brand-name">The<br>Road<br>Maven</p>

  <ul class="service-list service-list--right">
    <li><svg viewBox="0 0 26 26"><circle cx="13" cy="13" r="10.5" fill="none" stroke="#fbd40a" stroke-width="3"/><path d="M8 13.5l3.5 3.5 6.5-7" fill="none" stroke="#fbd40a" stroke-width="3"/></svg>PAVEMENT PEPAIRS</li>
    <li><svg viewBox="0 0 26 26"><circle cx="13" cy="13" r="10.5" fill="none" stroke="#fbd40a" stroke-width="3"/><path d="M8 13.5l3.5 3.5 6.5-7" fill="none" stroke="#fbd40a" stroke-width="3"/></svg>CONCREATE SIDEWALKS</li>
    <li><svg viewBox="0 0 26 26"><circle cx="13" cy="13" r="10.5" fill="none" stroke="#fbd40a" stroke-width="3"/><path d="M8 13.5l3.5 3.5 6.5-7" fill="none" stroke="#fbd40a" stroke-width="3"/></svg>PAVEMENT MARKINGS</li>
    <li><svg viewBox="0 0 26 26"><circle cx="13" cy="13" r="10.5" fill="none" stroke="#fbd40a" stroke-width="3"/><path d="M8 13.5l3.5 3.5 6.5-7" fill="none" stroke="#fbd40a" stroke-width="3"/></svg>PAVEMENT MAINTENANCE</li>
  </ul>

  <div class="feature-band"></div>
  <div class="feature-divider" style="left:370px"></div>
  <div class="feature-divider" style="left:596px"></div>
  <div class="feature-divider" style="left:828px"></div>

  <div class="feature-icon" style="left:174px">
    <svg viewBox="0 0 44 44"><path d="M10 18a12 12 0 0 1 22-5" fill="none" stroke="#fbd40a" stroke-width="3"/><path d="M34 8v7h-7" fill="none" stroke="#fbd40a" stroke-width="3"/><circle cx="22" cy="19" r="5" fill="#fff"/><path d="M6 34h8l8 4 14-6" fill="none" stroke="#fff" stroke-width="3"/></svg>
  </div>
  <div class="feature-icon" style="left:431px">
    <svg viewBox="0 0 44 44"><circle cx="20" cy="6" r="4" fill="#fff"/><path d="M20 12v14h10l4 10" fill="none" stroke="#fff" stroke-width="4"/><path d="M14 20a11 11 0 1 0 14 14" fill="none" stroke="#fbd40a" stroke-width="4"/></svg>
  </div>
  <div class="feature-icon" style="left:669px">
    <svg viewBox="0 0 44 44"><rect x="6" y="6" width="26" height="34" rx="2" fill="none" stroke="#fff" stroke-width="3"/><path d="M11 15h16M11 22h16M11 29h10" stroke="#fff" stroke-width="2.5"/><circle cx="33" cy="33" r="8" fill="#fbd40a"/><path d="M29 33l3 3 5-6" fill="none" stroke="#111" stroke-width="2.5"/></svg>
  </div>
  <div class="feature-icon" style="left:926px">
    <svg viewBox="0 0 44 44"><path d="M4 22l11-9 11 9v10H4z" fill="none" stroke="#fff" stroke-width="3"/><circle cx="33" cy="14" r="8" fill="#fbd40a"/><path d="M33 9v10" stroke="#111" stroke-width="2"/><path d="M4 38h30l6-5" fill="none" stroke="#fff" stroke-width="3"/></svg>
  </div>

  <p class="feature-label" style="left:105px">PROFESSIONALLY<br>MANAGED</p>
  <p class="feature-label" style="left:359px">ADA<br>COMPLIANCE</p>
  <p class="feature-label" style="left:597px">SITE<br>EVALUATIONS</p>
  <p class="feature-label" style="left:851px">PROJECT &amp; ASSET<br>MANAGEMENT</p>

  <div class="lane-line"></div>

  <p class="website">www.RoadMaven.com</p>
  <div class="social"><span></span><span></span><span></span></div>
</main>
</body>
</html>
```